Movix3 24/7 Gym & Health Bar Webpage

We need a professional and interactive webpage for a 24/7 health club.
Our approach is professional yet friendly offering holitic professional services for both general and special populations, along with flexible 24/7 gym and group fitness memberships. Professional services that we offer;
Exercise Physiologist
Strength & Conditioning
Physiotherapy
Chiropractor
Nutrition
Personal Training
we also service acute and chronic injuries, work cover, and veteran affairs

We also have a well-being bar offers healthy food, beverages and wide range of supplements.
We send out regular newsletters and want it to be interactive with social media and e-commerce.
Final design should demonstrate a holistic approach where clients have access to a wide range of health services within a professional health club environment. needs to be phone and table friendly please

i have attached a template i had been working on but wasn't happy with it

Target Market(s)

wide demographic including:

Special population - older demographic looking for professional services. Doctors will be referring clients to us also

24/7 gym - aged 25+ yrs, male and female

Industry/Entity Type

Health And Wellness

Coding

Coded - Design and coding required

Number of Pages Required

5+ page

Colors
33a6d7
add136
ffffff
0355a3

Requirements
Must have
• atmosphere and professionalism whilst inviting and sincere
• social media interaction & blog page
• clear navigation
• mobile and table friendly
• Tidal E-newsletter sign up
• testimonials
Nice to have
• customer feedback option
• FAQ
• opportunity to integrate online shop
• ability to download free visit pass

```html
<!DOCTYPE html>
<html lang="en">
<head>
<meta charset="utf-8">
<title>Movix3 24/7 Gym &amp; Health Bar</title>
<link rel="stylesheet" href="https://fonts.googleapis.com/css2?family=Oswald:wght@300;400;500&family=Raleway:wght@500;700&family=Roboto:wght@400;500;700&display=swap">
<style>
:root{
  --blue:#33a6d7;
  --blue-deep:#0355a3;
  --green:#add136;
  --white:#ffffff;
  --ink:#1c1c1c;
  --muted:#6b6b6b;
  --black:#000000;
  --grey-text:#c9c9c9;
  --red:#d9241c;
}
*{box-sizing:border-box;margin:0;padding:0}
html,body{width:1200px;height:2314px;overflow:hidden}
body{position:relative;background:var(--black);font-family:'Roboto',Arial,sans-serif;color:var(--white)}
section,header,footer{position:absolute;left:0;width:1200px}
.abs{position:absolute}

/* header */
.site-header{top:0;height:126px;background:linear-gradient(#ffffff,#f1f1f1);border-bottom:1px solid #ddd}
.brand{left:88px;top:30px;display:flex;align-items:center;gap:12px}
.brand-mark{width:50px;height:50px;border-radius:50%;background:var(--blue-deep)}
.brand-name{font-family:'Roboto',sans-serif;font-weight:700;font-size:44px;color:var(--blue);line-height:1}
.brand-sub{left:90px;top:90px;font-size:11px;font-weight:400;letter-spacing:1px;text-transform:uppercase;color:var(--muted)}
.main-nav{left:0;top:58px;width:1200px;font-size:14px;color:var(--ink)}
.main-nav a{position:absolute;color:var(--ink);text-decoration:none;white-space:nowrap}
.main-nav a.is-active{color:var(--blue)}

/* hero */
.hero{top:126px;height:571px;overflow:hidden}
.hero-photo{position:absolute;inset:0;background:linear-gradient(90deg,#6c5a52 0%,#8a7567 30%,#9fb6c4 55%,#7fb6d8 75%,#a9d2ea 100%)}
.hero-title{right:125px;top:240px;text-align:right;font-family:'Oswald',sans-serif;font-weight:400;font-size:48px;line-height:61px;color:var(--white);text-shadow:0 2px 6px rgba(0,0,0,.45);letter-spacing:-.5px}
.hero-cta{left:740px;top:386px;width:333px;height:69px;border-radius:6px;background:linear-gradient(#3cb0e6,#1d7fc4);box-shadow:0 3px 8px rgba(0,0,0,.3);display:flex;align-items:center;padding-left:24px;font-family:'Roboto',sans-serif;font-weight:500;font-size:18px;color:var(--white)}
.hero-cta .chev{position:absolute;right:22px;top:20px;width:30px;height:30px;border-radius:50%;background:#1a67a4}
.hero-arrow{top:290px}

/* intro */
.intro{top:697px;height:255px;background:var(--black);text-align:center}
.intro h1{position:absolute;top:32px;width:100%;font-family:'Raleway',sans-serif;font-weight:500;font-size:22px;color:var(--green)}
.intro .copy{position:absolute;left:80px;width:1040px;top:88px;font-size:14px;line-height:24px;color:#e4e4e4;letter-spacing:-.1px}
.intro .copy p+p{margin-top:12px}

/* features */
.features{top:952px;height:482px;background:linear-gradient(#3a3a3a,#121212);border-top:6px solid #1f4d6b}
.feature{top:52px;width:327px}
.feature-photo{width:327px;height:191px;border:3px solid var(--white)}
.feature h2{margin-top:30px;font-family:'Oswald',sans-serif;font-weight:400;font-size:22px;color:var(--green)}
.feature p{margin-top:14px;width:295px;font-size:13px;line-height:19px;color:var(--grey-text);text-align:justify}
.btn-small{display:inline-block;margin-top:18px;width:105px;height:36px;line-height:36px;text-align:center;border-radius:3px;background:linear-gradient(#2f8fd6,#1562a8);font-size:14px;font-weight:500;color:var(--white)}

/* blogs */
.blogs{top:1434px;height:324px;overflow:hidden}
.blogs-photo{position:absolute;inset:0;background:linear-gradient(90deg,#3d4c55 0%,#586771 45%,#8c959a 70%,#4a5256 100%)}
.blogs-shade{position:absolute;inset:0;background:rgba(15,25,35,.45)}
.blogs h2{position:absolute;top:20px;width:100%;text-align:center;font-family:'Oswald',sans-serif;font-weight:400;font-size:31px;color:var(--white)}
.blogs h2 span{color:var(--blue);font-weight:300}
.post{top:111px;display:flex;gap:22px}
.post-thumb{width:163px;height:139px;border:3px solid var(--white);border-radius:6px;flex:none}
.post-body{width:320px;padding-top:4px}
.post h3{font-family:'Raleway',sans-serif;font-weight:500;font-size:16px;color:var(--green)}
.post p{margin-top:12px;font-size:12px;line-height:22px;color:var(--white)}
.post .more{margin-top:6px;font-size:13px;color:var(--blue)}

/* newsletter */
.newsletter{top:1758px;height:150px;background:var(--green);border-top:4px solid #1f4d6b}
.newsletter h2{position:absolute;left:94px;top:48px;font-family:'Raleway',sans-serif;font-weight:700;font-size:23px}
.newsletter .sub{position:absolute;left:94px;top:82px;font-size:13.5px;font-weight:700}
.email-field{left:631px;top:60px;width:325px;height:42px;background:var(--white);border:1px solid #ccc;padding-left:16px;line-height:40px;font-size:12px;color:#555}
.signup-btn{left:976px;top:60px;width:130px;height:42px;background:var(--red);line-height:42px;text-align:center;font-size:16px;font-weight:500}

/* testimonial */
.testimonial{top:1908px;height:275px;overflow:hidden}
.testimonial-photo{position:absolute;inset:0;background:linear-gradient(90deg,#555f66,#737d84 50%,#5c666d)}
.testimonial-shade{position:absolute;inset:0;background:rgba(20,28,36,.55)}
.avatar{left:86px;top:65px;width:148px;height:148px;border-radius:50%;border:4px solid var(--white);background:linear-gradient(#b58b6c,#7e5a44)}
.quote-mark{left:236px;top:70px;font-family:'Oswald',sans-serif;font-size:44px;line-height:1}
.quote{left:265px;top:79px;width:850px;font-size:13.5px;line-height:27px}
.cite{left:270px;top:190px;font-family:'Oswald',sans-serif;font-size:18px;color:var(--green)}
.cite em{font-family:'Roboto',sans-serif;font-size:16px;font-style:italic;font-weight:400}
.dot{top:223px;width:16px;height:16px;border-radius:50%;border:2px solid var(--white)}
.dot.is-active{background:var(--green);border-color:var(--green)}

/* footer */
.site-footer{top:2183px;height:131px;background:var(--black)}
.footer-links{left:88px;top:43px;font-size:12.5px;color:var(--white)}
.footer-links span{margin:0 8px}
.copyright{left:88px;top:67px;font-size:12.5px}
.social{top:35px;width:28px;height:28px;border-radius:3px}
</style>
</head>
<body>

<header class="site-header">
  <div class="abs brand"><span class="brand-mark"></span><span class="brand-name">Movix3</span></div>
  <div class="abs brand-sub">Open 24/7 for every body</div>
  <nav class="abs main-nav">
    <a class="is-active" style="left:501px">HOME</a>
    <a style="left:572px">ABOUT</a>
    <a style="left:646px">SERVICES</a>
    <a style="left:742px">EVENTS</a>
    <a style="left:822px">SHOP</a>
    <a style="left:887px">CONTACT US</a>
    <a style="left:1003px">CLASSES</a>
    <svg class="abs" style="left:1088px;top:-3px" width="22" height="22" viewBox="0 0 22 22" aria-label="Search"><circle cx="9" cy="9" r="6.5" fill="none" stroke="#1c1c1c" stroke-width="3"/><line x1="14" y1="14" x2="20" y2="20" stroke="#1c1c1c" stroke-width="3.5" stroke-linecap="round"/></svg>
  </nav>
</header>

<section class="hero">
  <div class="hero-photo" role="img" aria-label="Smiling couple holding dumbbells in front of a group fitness class"></div>
  <svg class="abs hero-arrow" style="left:50px" width="32" height="64" viewBox="0 0 32 64" aria-label="Previous slide"><polyline points="28,2 4,32 28,62" fill="none" stroke="#fff" stroke-width="2"/></svg>
  <svg class="abs hero-arrow" style="left:1118px" width="32" height="64" viewBox="0 0 32 64" aria-label="Next slide"><polyline points="4,2 28,32 4,62" fill="none" stroke="#fff" stroke-width="2"/></svg>
  <h2 class="abs hero-title">MOVIX3 YOUR HEALTH<br>AND FITNESS</h2>
  <div class="abs hero-cta">DOWNLOAD FREE VISIT PASS
    <span class="chev"><svg width="30" height="30" viewBox="0 0 30 30"><polyline points="10,12 15,18 20,12" fill="none" stroke="#fff" stroke-width="2"/></svg></span>
  </div>
</section>

<section class="intro">
  <h1>MOVIX3 YOUR HEALTH AND FITNESS TODAY</h1>
  <div class="copy">
    <p>Movix3 was established in 2005 to offer individuals and groups quality health and fitness services in the Harbour Shire. Since then we have been growing and have now in 2012 moved to new bigger premises in Westbrook where we now offer new services alongside our proven solutions based personal training system.</p>
    <p>We now have the Movix3 Cafe, serving up not just great coffee, but also a wide range of healthy snacks and meals. Grab a post workout smoothie (low cal! we are a gym afterall), or take your time with a coffee and a wrap. Don't feel like a workout, no worries, the coffee still tastes great!</p>
  </div>
</section>

<section class="features">
  <article class="abs feature" style="left:89px">
    <div class="feature-photo" role="img" aria-label="Group stretching class in a bright studio" style="background:linear-gradient(120deg,#c9dce6,#e8d2c2 55%,#5f9fc8)"></div>
    <h2>SPECIAL OFFERS</h2>
    <p>Lorem Ipsum has been the industry's standard dummy text ever since the 1500s, when an unknown printer took a galley of type</p>
    <span class="btn-small">Read More</span>
  </article>
  <article class="abs feature" style="left:437px">
    <div class="feature-photo" role="img" aria-label="Woman jogging along the beach" style="background:linear-gradient(#dfeef5 0%,#cfe6ef 55%,#7fc3cf 70%,#e9e2d4 100%)"></div>
    <h2>MOVIX3 CAFE</h2>
    <p>Lorem Ipsum has been the industry's standard dummy text ever since the 1500s, when an unknown printer took a galley of type</p>
    <span class="btn-small">View More</span>
  </article>
  <article class="abs feature" style="left:785px">
    <div class="feature-photo" role="img" aria-label="Video of an aerobics class" style="background:linear-gradient(#b9c8d2,#6f7e88 70%,#2d3338)">
      <svg width="321" height="185" viewBox="0 0 321 185"><circle cx="148" cy="86" r="26" fill="rgba(60,60,60,.8)"/><polygon points="140,72 140,100 162,86" fill="#fff"/><rect x="0" y="167" width="321" height="18" fill="rgba(0,0,0,.6)"/><line x1="10" y1="176" x2="311" y2="176" stroke="#aaa" stroke-width="2"/></svg>
    </div>
    <h2>FEATURES AND SERVICES</h2>
    <p>Lorem Ipsum has been the industry's standard dummy text ever since the 1500s, when an unknown printer took a galley of type</p>
    <span class="btn-small">View More</span>
  </article>
</section>

<section class="blogs">
  <div class="blogs-photo" role="img" aria-label="Woman training with dumbbells in a gym"></div>
  <div class="blogs-shade"></div>
  <h2><span>LATEST</span> BLOGS</h2>
  <article class="abs post" style="left:91px">
    <div class="post-thumb" role="img" aria-label="Woman running on a treadmill" style="background:linear-gradient(#d7dde0,#7d8a92)"></div>
    <div class="post-body">
      <h3>IPSUM IS SIMPLY DUMMY TEXT</h3>
      <p>Lorem Ipsum is simply dummy text of the printing and typesetting industry. Lorem Ipsum has been the industry's standard dummy text ever since the 1500s, when</p>
      <div class="more">VIEW MORE &gt;&gt;</div>
    </div>
  </article>
  <article class="abs post" style="left:623px">
    <div class="post-thumb" role="img" aria-label="Group doing sit-ups on mats" style="background:linear-gradient(#c7b79a,#e08a3c 60%,#3f8fc9)"></div>
    <div class="post-body">
      <h3>IPSUM IS SIMPLY DUMMY TEXT</h3>
      <p>Lorem Ipsum is simply dummy text of the printing and typesetting industry. Lorem Ipsum has been the industry's standard dummy text ever since the 1500s, when</p>
      <div class="more">VIEW MORE &gt;&gt;</div>
    </div>
  </article>
</section>

<section class="newsletter">
  <h2>NEWSLETTER SIGNUP</h2>
  <div class="sub">Lorem Ipsum is simply dummy text of the printing and typesetting industry</div>
  <div class="abs email-field">Enter Your Email Address</div>
  <div class="abs signup-btn">SIGN UP</div>
</section>

<section class="testimonial">
  <div class="testimonial-photo" role="img" aria-label="Gym interior with training equipment"></div>
  <div class="testimonial-shade"></div>
  <div class="abs avatar" role="img" aria-label="Portrait of the club manager"></div>
  <div class="abs quote-mark">&ldquo;</div>
  <p class="abs quote">Lorem Ipsum has been the industry's standard dummy text ever since the 1500s, when an unknown printer took a galley of type and scrambled it to make a type specimen book. It has survived not only five centuries, but also the leap into electronic typesetting, remaining essentially unchanged. It was popularised in the 1960s with the release of Typeworks sheets containing Lorem Ipsum passages, and more recently with desktop publishing software like Folio Layout including versions of Lorem Ipsum.</p>
  <div class="abs cite">Maren <em>Manager</em></div>
  <span class="abs dot" style="left:1015px"></span>
  <span class="abs dot is-active" style="left:1042px"></span>
  <span class="abs dot" style="left:1068px"></span>
</section>

<footer class="site-footer">
  <div class="abs footer-links">Privacy Policy<span>|</span>Terms of Use<span>|</span>About Us<span>|</span>Sitemap</div>
  <div class="abs copyright">Copyright &copy; 2015 All Rights</div>
  <span class="abs social" style="left:966px;background:#1da1f2" role="img" aria-label="Social link"></span>
  <span class="abs social" style="left:1003px;background:#d8261c" role="img" aria-label="Video channel link"></span>
  <span class="abs social" style="left:1040px;background:#3b5998" role="img" aria-label="Social link"></span>
  <span class="abs social" style="left:1077px;background:#0a66a8" role="img" aria-label="Professional network link"></span>
</footer>

</body>
</html>
```